Roofing Company Sales Rep Business Card

Business card for sales rep to canvass and hand out to property owners/managers for free roof inspections and roof replacements.

```html
<!DOCTYPE html>
<html lang="en">
<head>
<meta charset="utf-8">
<title>Ridgeline Roofing – Business Card</title>
<link href="https://fonts.googleapis.com/css2?family=Montserrat:wght@400;500;600;800&display=swap" rel="stylesheet">
<style>
  :root {
    --ink: #1b1a1c;
    --paper: #ffffff;
    --accent: #e41e26;
    --stage: #3a3a3c;
    --text-light: #f2f2f2;
  }
  * { box-sizing: border-box; margin: 0; padding: 0; }
  html, body { width: 1200px; height: 900px; overflow: hidden; }
  body {
    background: var(--stage);
    font-family: "Montserrat", Arial, sans-serif;
    position: relative;
  }
  .card {
    position: absolute;
    top: 135px;
    width: 360px;
    height: 630px;
    overflow: hidden;
    background: var(--ink);
  }
  .card--front { left: 190px; }
  .card--back { left: 650px; }

  .card__band {
    position: absolute;
    left: 0; right: 0; bottom: 0;
    height: 16px;
    background: var(--accent);
  }

  .wordmark {
    display: flex;
    align-items: center;
    justify-content: center;
    gap: 10px;
    font-weight: 800;
    font-size: 27px;
    letter-spacing: 1px;
    text-transform: uppercase;
  }
  .wordmark__square {
    width: 16px; height: 16px;
    background: var(--accent);
  }

  /* Front */
  .front__brand {
    position: absolute;
    left: 0; right: 0; top: 0;
    height: 270px;
    background: var(--paper);
    display: flex;
    align-items: center;
    justify-content: center;
  }
  .front__brand .wordmark { color: var(--ink); }

  .front__info {
    position: absolute;
    left: 0; right: 0; top: 270px; bottom: 16px;
    display: flex;
    flex-direction: column;
    align-items: center;
    color: var(--text-light);
    text-align: center;
    padding-top: 36px;
  }
  .person__name {
    color: var(--accent);
    font-weight: 600;
    font-size: 30px;
    letter-spacing: 1px;
    text-transform: uppercase;
    line-height: 1;
  }
  .person__role {
    font-weight: 400;
    font-size: 16px;
    letter-spacing: 1px;
    margin-top: 6px;
  }
  .divider {
    display: flex;
    align-items: center;
    gap: 8px;
    margin-top: 26px;
  }
  .divider__line {
    width: 60px;
    height: 2px;
    background: var(--accent);
  }
  .divider__icon {
    width: 24px; height: 24px;
    border: 2px solid var(--accent);
    border-radius: 50%;
    display: flex; align-items: center; justify-content: center;
  }
  .divider__icon svg { width: 13px; height: 13px; }
  .contact {
    list-style: none;
    margin-top: 12px;
    font-size: 16px;
    line-height: 1.55;
    font-weight: 500;
  }
  .address {
    margin-top: 12px;
    font-size: 16px;
    line-height: 1.5;
    font-weight: 500;
  }

  /* Back */
  .card--back .wordmark {
    position: absolute;
    left: 0; right: 0; top: 210px;
    color: var(--text-light);
  }
</style>
</head>
<body>

  <article class="card card--front">
    <header class="front__brand">
      <div class="wordmark"><span class="wordmark__square"></span>Ridgeline Roofing</div>
    </header>

    <section class="front__info">
      <h1 class="person__name">Dana Reyes</h1>
      <p class="person__role">MANAGER</p>

      <div class="divider">
        <span class="divider__line"></span>
        <span class="divider__icon">
          <svg viewBox="0 0 16 16" aria-hidden="true"><path d="M3 1.5l3 3-1.6 1.8a9 9 0 0 0 5.3 5.3L11.5 10l3 3-2 2C7 14.5 1.5 9 1 3.5z" fill="var(--accent)"/></svg>
        </span>
        <span class="divider__icon">
          <svg viewBox="0 0 16 16" aria-hidden="true"><rect x="1" y="3" width="14" height="10" rx="1" fill="none" stroke="var(--accent)" stroke-width="1.8"/><path d="M1.5 3.5L8 9l6.5-5.5" fill="none" stroke="var(--accent)" stroke-width="1.8"/></svg>
        </span>
        <span class="divider__icon">
          <svg viewBox="0 0 16 16" aria-hidden="true"><circle cx="8" cy="8" r="6.5" fill="none" stroke="var(--accent)" stroke-width="1.6"/><ellipse cx="8" cy="8" rx="2.8" ry="6.5" fill="none" stroke="var(--accent)" stroke-width="1.4"/><path d="M1.5 8h13" stroke="var(--accent)" stroke-width="1.4"/></svg>
        </span>
        <span class="divider__line"></span>
      </div>

      <ul class="contact">
        <li>555-014-2278</li>
        <li>info@ridgelineroof.co</li>
        <li>www.ridgelineroof.co</li>
      </ul>

      <div class="divider">
        <span class="divider__line" style="width:90px"></span>
        <span class="divider__icon">
          <svg viewBox="0 0 16 16" aria-hidden="true"><path d="M8 15s5-5.2 5-8.5A5 5 0 0 0 3 6.5C3 9.8 8 15 8 15z" fill="none" stroke="var(--accent)" stroke-width="1.8"/><circle cx="8" cy="6.5" r="1.8" fill="var(--accent)"/></svg>
        </span>
        <span class="divider__line" style="width:90px"></span>
      </div>

      <p class="address">120 Harbor Lane<br>Springfield MA - 0100</p>
    </section>

    <div class="card__band"></div>
  </article>

  <article class="card card--back">
    <div class="wordmark"><span class="wordmark__square"></span>Ridgeline Roofing</div>
    <div class="card__band"></div>
  </article>

</body>
</html>
```